Business Card Design Project

We need a business card design for a new boutique consulting company, LumaConsulting. Our new logo has just been designed and we are looking for simple, clean looking business cards. Logo attached

Industry/Entity Type

Boutique

Requirements
Must have
• There must be room for each card to have the following details:
Name
Title
Address - 2 lines
Phone number
Email address
Website address

Nice to have
• May have something on the back of the buisness card - emphasing the word "Luma".

```html
<!DOCTYPE html>
<html lang="en">
<head>
<meta charset="utf-8">
<title>LumaConsulting — Business Card</title>
<link rel="stylesheet" href="https://fonts.googleapis.com/css2?family=Source+Sans+3:wght@400&display=swap">
<style>
  :root {
    --page: #ffffff;
    --frame: #333333;
    --card: #ffffff;
    --card-edge: #222222;
    --ink: #4a4a4a;
    --brand-green: #6dbf2e;
    --band-light: #8ad44a;
    --band-dark: #5cb526;
    --shadow: rgba(0, 0, 0, 0.55);
  }
  * { margin: 0; padding: 0; box-sizing: border-box; }
  html, body {
    width: 1200px;
    height: 849px;
    overflow: hidden;
    background: var(--page);
  }
  .sheet {
    position: relative;
    width: 1200px;
    height: 849px;
    border: 1px solid var(--frame);
    font-family: "Source Sans 3", "Helvetica Neue", Arial, sans-serif;
  }
  .card {
    position: absolute;
    background: var(--card);
    border: 1px solid var(--card-edge);
    box-shadow: 7px 8px 7px var(--shadow);
    overflow: hidden;
  }
  .card--front {
    left: 51px;
    top: 297px;
    width: 472px;
    height: 287px;
  }
  .card--back {
    left: 675px;
    top: 303px;
    width: 471px;
    height: 287px;
  }
  .brand-name {
    position: absolute;
    left: 10px;
    bottom: 18px;
    font-size: 66px;
    font-weight: 400;
    letter-spacing: -0.5px;
    line-height: 1;
    color: var(--brand-green);
  }
  .contact {
    position: absolute;
    left: 44px;
    top: 99px;
    list-style: none;
    font-size: 15px;
    line-height: 20.7px;
    color: var(--ink);
  }
  .accent-band {
    position: absolute;
    left: 0;
    right: 0;
    bottom: 0;
    height: 52px;
    background: linear-gradient(to bottom, var(--band-light), var(--band-dark));
  }
</style>
</head>
<body>
  <main class="sheet">
    <section class="card card--front" aria-label="Card front">
      <p class="brand-name">LumaConsulting</p>
    </section>

    <section class="card card--back" aria-label="Card back">
      <ul class="contact">
        <li class="contact__name">Sam Rivers</li>
        <li class="contact__street">42 Harbour Lane</li>
        <li class="contact__city">Brookfield 3100</li>
        <li class="contact__phone">09 55210 4417</li>
        <li class="contact__web">www.lumaconsulting.com</li>
        <li class="contact__email">sam@lumaconsulting.com</li>
      </ul>
      <div class="accent-band"></div>
    </section>
  </main>
</body>
</html>
```